Staff Falcons WIX Design Project - website for HR Professional Community

Redesign of website to incorporate new logo - we are looking for a web design partner - will include adhoc work going forward.

Current website - www.thestafffalcons.co.uk

The 'Onward to Radiant' content is not required on the new site.

Target Market(s)

HR professionals

Industry/Entity Type

Professional Network

Coding

Coded - Design and coding required

Requirements
Must have
• A partners page
Nice to have
• an events page

```html
<!DOCTYPE html>
<html lang="en">
<head>
<meta charset="utf-8">
<title>Staff Falcons – HR Professional Community</title>
<link rel="stylesheet" href="https://fonts.googleapis.com/css2?family=Poppins:ital,wght@0,400;0,500;0,600;0,700;1,400&display=swap">
<style>
:root{
  --orange:#f0841c;
  --orange-dark:#e0761a;
  --ink:#1e1e22;
  --text:#3a3a3a;
  --muted:#666;
  --beige:#f7f1ea;
  --footer:#1f1f23;
  --white:#fff;
}
*{box-sizing:border-box;margin:0;padding:0}
html,body{width:1200px;height:4587px;overflow:hidden}
body{font-family:'Poppins',sans-serif;color:var(--text);background:var(--white);position:relative}
.accent{color:var(--orange);font-weight:700}
.btn{position:absolute;display:flex;align-items:center;justify-content:center;gap:10px;background:var(--orange);color:#fff;font-weight:600;text-transform:uppercase;box-shadow:3px 3px 0 var(--orange-dark);letter-spacing:.3px}
.btn svg{width:24px;height:10px}
.arrow-link{position:absolute;color:var(--orange);font-size:12px;font-weight:600;text-transform:uppercase;display:flex;align-items:center;gap:8px;white-space:nowrap}
.arrow-link svg{width:20px;height:9px}

/* header */
.brand{position:absolute;display:flex;flex-direction:column;align-items:center}
.brand-mark{border-radius:50%;background:var(--orange)}
.brand-name{font-weight:500;color:var(--ink);letter-spacing:2px;white-space:nowrap}
.top-info{position:absolute;top:12px;display:flex;align-items:center;gap:12px}
.top-info .ico{width:34px;height:34px;border-radius:50%;background:var(--orange);display:flex;align-items:center;justify-content:center}
.top-info small{display:block;font-size:10px;color:var(--muted)}
.top-info b{display:block;font-size:14px;font-weight:500;color:var(--ink)}
.nav{position:absolute;left:326px;top:75px;width:874px;height:39px;background:var(--beige);display:flex;align-items:center;padding-left:40px}
.nav a{font-size:12px;font-weight:500;color:var(--ink);text-decoration:none;text-transform:uppercase;margin-right:58px}
.nav a.active{color:var(--orange)}

/* hero */
.hero{position:absolute;top:114px;left:0;width:1200px;height:637px;background:linear-gradient(180deg,#eef0f4 0%,#e4e6eb 55%,#d9d6d2 100%)}
.hero-title{position:absolute;top:70px;width:100%;text-align:center;font-size:66px;font-weight:400;color:var(--ink);letter-spacing:1px}
.hero-sub{position:absolute;top:152px;width:100%;text-align:center;font-size:22px;color:var(--ink)}
.hero-people{position:absolute;left:80px;top:300px;width:1040px;height:337px;border-radius:180px 180px 0 0;background:linear-gradient(180deg,#c7b6a6 0%,#5f7da8 45%,#2c3e5c 100%);opacity:.85}

.sec-title{position:absolute;width:100%;text-align:center;font-size:42px;color:var(--ink);font-weight:400}

/* services */
.card{position:absolute;top:917px;width:315px;height:477px;background:#fff;box-shadow:0 6px 18px rgba(0,0,0,.1);border-right:5px solid var(--orange)}
.card .photo{height:272px;width:100%}
.card .icon{position:absolute;left:50%;top:186px;transform:translateX(-50%);width:78px;height:78px;border-radius:50%;background:var(--orange);border:5px solid #fff;display:flex;align-items:center;justify-content:center}
.card h3{position:absolute;top:277px;width:100%;text-align:center;font-size:21px;font-weight:600;color:var(--ink)}
.card p{position:absolute;top:322px;left:38px;right:38px;text-align:center;font-size:13px;line-height:24px;color:var(--text)}
.card .arrow-link{left:0;right:0;justify-content:center;top:444px}

/* job board */
.jb-band{position:absolute;left:0;top:1490px;width:555px;height:755px;background:var(--orange)}
.jb-photo{position:absolute;left:137px;top:1598px;width:502px;height:490px;background:linear-gradient(135deg,#8d97a3,#3d4d66 55%,#c9b8a8)}
.dots{position:absolute;left:572px;top:1573px;width:120px;height:76px;background-image:radial-gradient(#9aa 1.3px,transparent 1.5px);background-size:12px 12px}
.jb-text{position:absolute;left:748px;top:1628px;width:420px}
.jb-text h2{font-size:40px;line-height:48px;font-weight:400;color:var(--ink);white-space:nowrap}
.jb-text .lead{margin-top:22px;font-size:12.5px;line-height:27px;color:var(--ink);white-space:nowrap}
.jb-text .hl{margin-top:10px;width:360px;font-size:19px;line-height:32px;color:var(--orange);font-weight:500}
.jb-text .note{margin-top:10px;width:360px;font-size:12px;line-height:27px;color:var(--ink)}
.jb-text .btn{position:relative;margin-top:40px;width:134px;height:34px;font-size:9px}

/* team */
.member{position:absolute;top:2438px;width:260px;text-align:center}
.avatar{width:246px;height:246px;margin:0 auto;border-radius:50%;border:7px solid transparent;border-top-color:var(--orange);border-right-color:var(--orange);padding:5px}
.avatar div{width:100%;height:100%;border-radius:50%;background:linear-gradient(160deg,#d8d8d8,#7a7a7a)}
.member h4{margin-top:16px;font-size:22px;font-weight:600;color:var(--ink)}
.member span{display:block;font-size:15px;color:var(--ink);margin-top:2px}
.member .soc{display:block;width:18px;height:18px;border-radius:50%;background:var(--orange);margin:12px auto 0}

/* testimonials */
.testi-bg{position:absolute;left:0;top:2887px;width:1200px;height:639px;background:linear-gradient(135deg,#f4f4f5,#ececee 50%,#f6f6f7)}
.testi-title{position:absolute;top:2950px;width:100%;text-align:center;font-size:40px;line-height:46px;color:var(--ink);font-weight:400}
.quote{position:absolute;top:3074px;width:477px;height:361px;background:#fff;border-radius:18px;box-shadow:0 4px 20px rgba(0,0,0,.06);padding:34px 32px}
.quote svg{display:block}
.quote p{margin-top:14px;font-size:15.5px;line-height:34px;font-style:italic;color:var(--ink)}
.quote .who{margin-top:14px;font-size:16px;color:var(--ink)}
.quote .who b{font-weight:600}
.stars{margin-top:2px;color:var(--orange);font-size:14px;letter-spacing:2px}

/* contact */
.contact-bg{position:absolute;left:0;top:3526px;width:1200px;height:632px;background:var(--orange)}
.contact-photo{position:absolute;left:0;top:3526px;width:650px;height:632px}
.contact-text{position:absolute;left:733px;top:3597px}
.contact-text small{display:block;font-size:21px;font-weight:600;color:#fff}
.contact-text h2{font-size:36px;font-weight:400;color:#fff;line-height:44px}
.field{position:absolute;left:740px;width:360px;height:40px;border:1.5px solid rgba(255,255,255,.8);color:#fff;font-size:11px;padding:12px 16px}
.btn-dark{position:absolute;left:740px;top:4033px;width:191px;height:41px;background:var(--ink);color:#fff;font-size:10px;font-weight:600;display:flex;align-items:center;justify-content:center;gap:10px;box-shadow:3px 3px 0 #000}

/* footer */
.footer{position:absolute;left:0;top:4158px;width:1200px;height:429px;background:var(--footer);color:#fff}
.footer h5{font-size:13px;font-weight:600;letter-spacing:.3px}
.footer .col{position:absolute;top:119px}
.footer p,.footer li{font-size:11px;line-height:20px;color:#ddd;list-style:none}
.ft-input{width:303px;height:40px;background:#fff;color:#555;font-size:11px;padding:12px 18px;margin-top:14px;box-shadow:3px 3px 0 var(--orange)}
.ft-line{display:flex;gap:14px;align-items:flex-start;margin-top:12px;font-size:11px;color:#ddd}
.ft-line svg{flex:0 0 12px;margin-top:3px}
.social{position:absolute;left:840px;top:4519px;display:flex;align-items:center;gap:8px}
.social span{font-size:13px;color:#fff;margin-right:16px}
.social i{width:27px;height:27px;border:1.5px solid #fff;border-radius:50%}
</style>
</head>
<body>

<!-- Header -->
<div class="brand" style="left:106px;top:6px">
  <div class="brand-mark" style="width:44px;height:44px"></div>
  <div class="brand-name" style="font-size:22px;margin-top:8px">STAFF FALCONS</div>
</div>
<div class="top-info" style="left:544px">
  <div class="ico"><svg width="16" height="16" viewBox="0 0 24 24" fill="#fff"><path d="M6.6 10.8a15 15 0 006.6 6.6l2.2-2.2a1 1 0 011-.25 11.4 11.4 0 003.6.57 1 1 0 011 1V20a1 1 0 01-1 1A17 17 0 013 4a1 1 0 011-1h3.5a1 1 0 011 1c0 1.25.2 2.45.57 3.57a1 1 0 01-.25 1z"/></svg></div>
  <div><small>Have any question?</small><b>+888 888 8888</b></div>
</div>
<div class="top-info" style="left:727px">
  <div class="ico"><svg width="16" height="14" viewBox="0 0 24 20" fill="none" stroke="#fff" stroke-width="2"><rect x="2" y="2" width="20" height="16" rx="2"/><path d="M2 4l10 7 10-7"/></svg></div>
  <div><small>Mail us:</small><b>hq@thestafffalcons.co.uk</b></div>
</div>
<div class="btn" style="left:960px;top:10px;width:136px;height:38px;font-size:12px">View Jobs <svg viewBox="0 0 24 10" fill="none" stroke="#fff" stroke-width="1.5"><path d="M0 5h22M18 1l4 4-4 4"/></svg></div>
<nav class="nav">
  <a class="active">Home</a><a>Our Story</a><a>Jobs</a><a>Team</a><a>Review</a><a>Newsletter</a><a>Contact</a>
</nav>

<!-- Hero -->
<section class="hero">
  <h1 class="hero-title"><span class="accent">THE STAFF</span> FALCONS!</h1>
  <p class="hero-sub">The UK's most vibrant online community for HR Professionals.</p>
  <div class="btn" style="left:522px;top:215px;width:155px;height:37px;font-size:12px">Get Started <svg viewBox="0 0 24 10" fill="none" stroke="#fff" stroke-width="1.5"><path d="M0 5h22M18 1l4 4-4 4"/></svg></div>
  <div class="hero-people" role="img" aria-label="Five smiling HR professionals seated in a row against a light wall"></div>
</section>

<!-- What we do -->
<h2 class="sec-title" style="top:828px"><span class="accent">WHAT</span> WE DO</h2>

<article class="card" style="left:100px">
  <div class="photo" role="img" aria-label="Many hands stacked together over a wooden table" style="background:linear-gradient(135deg,#5b3a26,#c89a72 55%,#e8d6c2)"></div>
  <div class="icon"><svg width="34" height="34" viewBox="0 0 24 24" fill="none" stroke="#fff" stroke-width="1.4"><circle cx="12" cy="7" r="3"/><circle cx="5" cy="10" r="2"/><circle cx="19" cy="10" r="2"/><path d="M6 20c0-4 3-7 6-7s6 3 6 7M1 18c0-3 2-5 4-5M23 18c0-3-2-5-4-5"/></svg></div>
  <h3>COMMUNITY</h3>
  <p>Our Circlebook Community Group enables you to connect with a fast-growing, highly engaged community of over 17k HR professionals</p>
  <div class="arrow-link">Join our Circlebook group <svg viewBox="0 0 24 10" fill="none" stroke="currentColor" stroke-width="1.5"><path d="M0 5h22M18 1l4 4-4 4"/></svg></div>
</article>

<article class="card" style="left:442px">
  <div class="photo" role="img" aria-label="Wooden blocks spelling jobs on a grey surface" style="background:linear-gradient(180deg,#2f3b4a,#7a8796 55%,#b89a78)"></div>
  <div class="icon"><svg width="32" height="32" viewBox="0 0 24 24" fill="none" stroke="#fff" stroke-width="1.5"><rect x="3" y="7" width="18" height="13" rx="2"/><path d="M9 7V5h6v2M3 12h18M11 12v2h2v-2"/></svg></div>
  <h3>JOBS</h3>
  <p>Get your HR job in front of 17k HR Professionals FREE job postings for members of our Circlebook group Open to non-members ONLY £100+vat</p>
  <div class="arrow-link">View our jobs board <svg viewBox="0 0 24 10" fill="none" stroke="currentColor" stroke-width="1.5"><path d="M0 5h22M18 1l4 4-4 4"/></svg></div>
</article>

<article class="card" style="left:785px">
  <div class="photo" role="img" aria-label="Coaching group meeting in a bright brick-walled office" style="background:linear-gradient(135deg,#3a2a22,#9c7656 45%,#d9c3a4)"></div>
  <div class="icon"><svg width="34" height="34" viewBox="0 0 24 24" fill="none" stroke="#fff" stroke-width="1.4"><rect x="5" y="2" width="14" height="9"/><circle cx="6" cy="15" r="1.6"/><circle cx="12" cy="15" r="1.6"/><circle cx="18" cy="15" r="1.6"/><path d="M3 21c0-2 1.3-3.5 3-3.5S9 19 9 21M9 21c0-2 1.3-3.5 3-3.5s3 1.5 3 3.5M15 21c0-2 1.3-3.5 3-3.5s3 1.5 3 3.5"/></svg></div>
  <h3>COACHING</h3>
  <p>Our coaching club is currently over subscribed and we are not currently accepting requests for support. Doors are open now for registrations!</p>
  <div class="arrow-link">Our coaching club <svg viewBox="0 0 24 10" fill="none" stroke="currentColor" stroke-width="1.5"><path d="M0 5h22M18 1l4 4-4 4"/></svg></div>
</article>

<!-- Job board -->
<div class="jb-band"></div>
<div class="dots"></div>
<div class="jb-photo" role="img" aria-label="Three colleagues smiling around a laptop in an office"></div>
<div class="jb-text">
  <h2><span class="accent">THE STAFF FALCONS</span><br>JOB BOARD!</h2>
  <p class="lead">Are you looking to share your HR roles with our audience?<br>Are you an HR job seeker looking for your next adventure?</p>
  <p class="hl">We are fast becoming THE place to share and seek for HR jobs in the UK</p>
  <p class="note">(and get this!... If you're a member of our Circlebook group you can share your jobs for FREE!)</p>
  <div class="btn">Learn More <svg viewBox="0 0 24 10" fill="none" stroke="#fff" stroke-width="1.5"><path d="M0 5h22M18 1l4 4-4 4"/></svg></div>
</div>

<!-- Team -->
<h2 class="sec-title" style="top:2338px"><span class="accent">MEET</span> OUR TEAM</h2>
<div class="member" style="left:116px">
  <div class="avatar"><div role="img" aria-label="Black and white portrait of the founder"></div></div>
  <h4>MARLA QUENNELL</h4><span>Founder The Staff Falcons</span><i class="soc"></i>
</div>
<div class="member" style="left:470px">
  <div class="avatar"><div role="img" aria-label="Black and white portrait of the head of partnerships"></div></div>
  <h4>DESMOND ARKWRIGHT</h4><span>Head of Partnerships</span><i class="soc"></i>
</div>
<div class="member" style="left:824px">
  <div class="avatar"><div role="img" aria-label="Black and white portrait of the creative editor"></div></div>
  <h4>TALIA BROOKVALE</h4><span>Creative Editor</span><i class="soc"></i>
</div>

<!-- Testimonials -->
<div class="testi-bg"></div>
<h2 class="testi-title"><span class="accent">WHAT THEY ARE TALKING</span><br>ABOUT OUR SERVICES</h2>
<div class="quote" style="left:110px">
  <svg width="42" height="34" viewBox="0 0 42 34" fill="var(--orange)"><path d="M0 34V20C0 8 6 2 16 0l2 5c-6 2-9 6-9 11h9v18zM24 34V20C24 8 30 2 40 0l2 5c-6 2-9 6-9 11h9v18z"/></svg>
  <p>I came across the Staff Falcons community on Circlebook and truly believe that the timing of this was meant to be because I asked for some advice relating to a role I was applying for and 8 days later I landed the job! I am blown away by the support in this group”</p>
  <div class="who"><b>Rosalind.</b> &nbsp;- &nbsp;HR Professional</div>
  <div class="stars">★★★★★</div>
</div>
<div class="quote" style="left:614px">
  <svg width="42" height="34" viewBox="0 0 42 34" fill="var(--orange)"><path d="M0 34V20C0 8 6 2 16 0l2 5c-6 2-9 6-9 11h9v18zM24 34V20C24 8 30 2 40 0l2 5c-6 2-9 6-9 11h9v18z"/></svg>
  <p>I came across the Staff Falcons community on Circlebook and truly believe that the timing of this was meant to be because I asked for some advice relating to a role I was applying for and 8 days later I landed the job! I am blown away by the support in this group”</p>
  <div class="who"><b>Rosalind.</b> &nbsp;- &nbsp;HR Professional</div>
  <div class="stars">★★★★★</div>
</div>

<!-- Contact -->
<div class="contact-bg"></div>
<svg class="contact-photo" viewBox="0 0 650 632" role="img" aria-label="Smiling woman working on a laptop in a cafe">
  <defs><linearGradient id="cp" x1="0" y1="0" x2="1" y2="1"><stop offset="0" stop-color="#4a3a2e"/><stop offset=".5" stop-color="#a8896f"/><stop offset="1" stop-color="#d8d2cc"/></linearGradient></defs>
  <polygon points="0,0 520,0 600,260 520,632 0,632" fill="url(#cp)"/>
  <polyline points="540,10 620,260 540,620" fill="none" stroke="#d9701a" stroke-width="3"/>
</svg>
<div class="contact-text"><small>CONTACT US</small><h2><b style="font-weight:700">GET IN</b> TOUCH</h2></div>
<div class="field" style="top:3706px">First name</div>
<div class="field" style="top:3763px">Phone</div>
<div class="field" style="top:3819px">Email address</div>
<div class="field" style="top:3876px">Company</div>
<div class="field" style="top:3932px;height:80px">Message</div>
<div class="btn-dark">REQUEST A ESTIMATE <svg width="24" height="10" viewBox="0 0 24 10" fill="none" stroke="#fff" stroke-width="1.5"><path d="M0 5h22M18 1l4 4-4 4"/></svg></div>

<!-- Footer -->
<footer class="footer">
  <div class="brand" style="left:104px;top:146px">
    <div class="brand-mark" style="width:46px;height:46px"></div>
    <div class="brand-name" style="font-size:25px;color:#fff;margin-top:10px">STAFF FALCONS</div>
  </div>
  <div class="col" style="left:377px;width:310px">
    <h5>STAFF FALCONS NEWSLETTER</h5>
    <p style="margin-top:12px">Sign up to hear from us. Sed ut perspiciatis unde omnis iste natus voluptatem accusantium, dolue laudantium,</p>
    <div class="ft-input">Your email address</div>
    <div class="btn" style="position:relative;margin-top:14px;width:148px;height:38px;font-size:10px">Subscribe <svg viewBox="0 0 24 10" fill="none" stroke="#fff" stroke-width="1.5"><path d="M0 5h22M18 1l4 4-4 4"/></svg></div>
  </div>
  <div class="col" style="left:758px;width:200px">
    <h5>CONTACT US</h5>
    <div class="ft-line" style="margin-top:16px"><svg width="12" height="14" viewBox="0 0 12 16" fill="var(--orange)"><path d="M6 0a6 6 0 016 6c0 4.5-6 10-6 10S0 10.5 0 6a6 6 0 016-6zm0 3.5a2.5 2.5 0 100 5 2.5 2.5 0 000-5z"/></svg><span>14 - 16 Harrowgate Lane<br>London E9 4QT</span></div>
    <div class="ft-line"><svg width="12" height="12" viewBox="0 0 24 24" fill="var(--orange)"><path d="M6.6 10.8a15 15 0 006.6 6.6l2.2-2.2a1 1 0 011-.25 11.4 11.4 0 003.6.57 1 1 0 011 1V20a1 1 0 01-1 1A17 17 0 013 4a1 1 0 011-1h3.5a1 1 0 011 1c0 1.25.2 2.45.57 3.57a1 1 0 01-.25 1z"/></svg><span>+888 888 8888</span></div>
    <div class="ft-line"><svg width="12" height="10" viewBox="0 0 24 20" fill="none" stroke="var(--orange)" stroke-width="2"><rect x="2" y="2" width="20" height="16" rx="2"/><path d="M2 4l10 7 10-7"/></svg><span>hq@thestafffalcons.co.uk</span></div>
  </div>
  <div class="col" style="left:1000px">
    <h5>USEFUL LINKS</h5>
    <ul style="margin-top:14px;line-height:24px">
      <li>Home</li><li>Our Story</li><li>Jobs</li><li>Team</li><li>Review</li><li>Newsletter</li><li>Contact</li>
    </ul>
  </div>
  <p style="position:absolute;left:98px;top:365px;font-size:13px;color:#fff">Copyright © The Staff Falcons 2022. All rights reserved.</p>
</footer>
<div class="social"><span>FOLLOW</span><i></i><i></i><i></i><i></i><i></i></div>

</body>
</html>
```